Tarrowby Builders Business Card Design

We require a business Card for a new Building Company called Tarrowby Builders. We are General Builders that specialize in Industrial, Commercial and Domestic building work. We would like to see a design that incorporates Blue ,Red and White as the colour scheme and a design that will highlight a building theme.
(Once this design is achieved will need to incorporate this for the other side of the business which is Tarrowby Joinery )

Industry/Entity Type

Business

Contact Information for Business Card

TARROWBY BUILDERS
17 Wendalee Rd Nuriootpa SA 5355
Mobile 0427390658
Telephone 08 85947316
Marcus Dewhirst
Director / Supervisor

```html
<!DOCTYPE html>
<html lang="en">
<head>
<meta charset="utf-8">
<title>Tarrowby Builders Business Card</title>
<link href="https://fonts.googleapis.com/css2?family=Arimo:wght@400;700&display=swap" rel="stylesheet">
<style>
  :root {
    --stage: #2b2b2d;
    --card: #ffffff;
    --navy: #1c2566;
    --ink: #1a1a1a;
    --block-red: #d9263a;
    --block-green: #2e9a3c;
    --block-yellow: #e6b619;
    --block-blue: #2356b0;
    --block-sky: #6fb3e3;
  }
  * { box-sizing: border-box; margin: 0; padding: 0; }
  html, body {
    width: 1200px; height: 900px; overflow: hidden;
    background: var(--stage);
    font-family: "Arimo", Arial, sans-serif;
  }
  .card {
    position: absolute;
    width: 560px; height: 320px;
    background: var(--card);
    border-radius: 16px;
    overflow: hidden;
    box-shadow: 0 10px 30px rgba(0,0,0,.45);
  }
  .card--back { left: 150px; top: 70px; }
  .card--front { left: 490px; top: 510px; }

  .blocks {
    position: absolute;
    background: linear-gradient(100deg, var(--block-red) 0%, var(--block-red) 25%, var(--block-green) 40%, var(--block-yellow) 60%, var(--block-blue) 82%, var(--block-sky) 100%);
    border-radius: 4px;
  }
  .card--back .blocks { left: 170px; top: 80px; width: 230px; height: 110px; }
  .website {
    position: absolute; left: 0; right: 0; top: 210px;
    text-align: center;
    color: var(--navy);
    font-size: 15px; letter-spacing: 2px;
  }

  .card--front .blocks--main { left: 40px; top: 18px; width: 250px; height: 140px; }
  .blocks--corner {
    position: absolute; right: 0; bottom: 0;
    width: 200px; height: 170px;
    background: linear-gradient(120deg, var(--block-sky) 0%, var(--block-blue) 30%, var(--block-yellow) 55%, var(--block-red) 80%);
    clip-path: polygon(100% 0, 100% 100%, 0 100%, 20% 70%, 60% 40%, 80% 10%);
  }
  .identity { position: absolute; left: 120px; top: 166px; }
  .identity__name { font-size: 26px; color: var(--ink); line-height: 1.05; }
  .identity__role { font-size: 16px; color: var(--navy); margin-top: 2px; }
  .rule {
    position: absolute; left: 60px; top: 222px; width: 300px; height: 1px;
    background: linear-gradient(90deg, rgba(0,0,0,0), rgba(0,0,0,.12), rgba(0,0,0,0));
  }
  .contact { position: absolute; left: 120px; top: 230px; font-size: 14px; color: var(--ink); line-height: 18px; }
  .contact__company { margin-left: 22px; }
  .contact__row { display: flex; align-items: center; gap: 8px; }
  .contact__icon { width: 14px; height: 14px; fill: var(--ink); flex: none; }
</style>
</head>
<body>
  <section class="card card--back">
    <div class="blocks" role="img" aria-label="Photo of colourful wooden toy building blocks arranged as a house"></div>
    <p class="website">www.tarrowbybuilders.com</p>
  </section>

  <section class="card card--front">
    <div class="blocks blocks--main" role="img" aria-label="Photo of colourful wooden toy building blocks arranged as a house"></div>
    <div class="blocks--corner" role="img" aria-label="Photo of scattered red, yellow and blue wooden blocks"></div>
    <div class="identity">
      <p class="identity__name">Marcus Dewhirst</p>
      <p class="identity__role">Director / Supervisor</p>
    </div>
    <div class="rule"></div>
    <div class="contact">
      <p class="contact__company">TARROWBY BUILDERS</p>
      <p class="contact__row">
        <svg class="contact__icon" viewBox="0 0 16 16"><path d="M8 1 1 7.5h2V15h4v-4h2v4h4V7.5h2z"/></svg>
        17 Wendalee Rd Kelbrook SA 5372
      </p>
      <p class="contact__row">
        <svg class="contact__icon" viewBox="0 0 16 16"><path d="M4 1h8v14H4zM5.5 2.5v9h5v-9z"/></svg>
        Mobile 0427390658
      </p>
      <p class="contact__row">
        <svg class="contact__icon" viewBox="0 0 16 16"><path d="M1 5c0-2 3-3 7-3s7 1 7 3v2h-4V5H5v2H1zM3 8h10l1 6H2z"/></svg>
        Telephone 08 85947316
      </p>
    </div>
  </section>
</body>
</html>
```